T&R Custom Homes and Remodeling Flyer

We need a new double sided flyer that showcases our service.
Our website is http://trhomesbuildco.example/
Please use the information on http://trhomesbuildco.example/about-us/ for the information in the flyer.
This handout will be used to give to our potential customers and needs to show the complete story of who we are and the services we provide. I have also attached pictures of project we have completed that should be used for the flyer.
Any other pictures can be taken from our photo gallery on the website.

Target Market(s)

Clients who want a custom home or remodel

Industry/Entity Type

Construction

Font styles to use
Serif

Requirements
Must have
• Prominent logo
• Pictures of completed projects
• Tri-fold design- eps file is attached for this
Nice to have
• Manly colors
• If you can find a tasteful way to add the picture of the owners that is great, but it should be small and is not necessary.
Should not have
• Pink/girly touches

```html
<!DOCTYPE html>
<html lang="en">
<head>
<meta charset="utf-8">
<title>T&amp;R Custom Homes and Remodeling – Tri-fold Flyer</title>
<link rel="stylesheet" href="https://fonts.googleapis.com/css2?family=Noto+Serif:ital,wght@0,400;0,700;1,700&display=swap">
<style>
:root{
  --navy:#243a5c;
  --charcoal:#2e2f33;
  --ink:#2b2b2b;
  --paper:#ffffff;
  --stage:#e9e9e9;
  --sky:#9dbbd6;
  --grass:#4f7b2c;
}
*{margin:0;padding:0;box-sizing:border-box}
html,body{width:1200px;height:1000px;overflow:hidden}
body{background:var(--stage);font-family:"Noto Serif",Georgia,serif;color:var(--ink);position:relative}
.sheet{position:absolute;left:305px;width:590px;height:456px;background:var(--paper);overflow:hidden;box-shadow:0 2px 6px rgba(0,0,0,.18)}
.sheet--outside{top:22px}
.sheet--inside{top:503px}
.abs{position:absolute}
.photo{position:absolute}
.label{position:absolute;background:var(--charcoal);color:#fff;font-size:8.5px;text-align:center;letter-spacing:.3px;display:flex;align-items:center;justify-content:center;line-height:1.25}
.body-text{position:absolute;font-size:7px;line-height:1.4;white-space:nowrap}
.body-text strong{color:var(--navy);font-weight:700}
.caps{text-transform:uppercase}
/* outside */
.panel-quality-top{left:0;top:0;width:195px;height:160px;background:var(--navy)}
.intro{left:20px;top:18px;width:168px;color:#fff;text-align:right;font-size:7px;line-height:1.42;white-space:nowrap}
.intro .lead{color:#d7dbe2}
.intro strong{font-weight:700}
.panel-detail{left:195px;top:0;width:197px;height:456px;background:var(--navy)}
.values-box{left:205px;top:0;width:130px;height:230px;background:var(--charcoal)}
.values{left:213px;top:78px;width:120px;color:#fff;font-size:6.6px;line-height:1.6;white-space:nowrap;letter-spacing:-.1px}
.values strong{font-weight:700}
.owners-card{left:291px;top:20px;width:84px;height:68px;background:#fff}
.owners-caption{left:291px;top:80px;width:84px;font-size:5px;font-weight:700;text-align:center;color:var(--ink)}
.fold-brand{left:195px;top:382px;width:197px;text-align:center;color:#fff}
.brand-name{font-weight:700;font-size:7px;letter-spacing:.3px;line-height:1.3}
.fold-brand .address{font-size:5.6px;margin-top:8px;line-height:1.6}
.panel-cover{left:392px;top:0;width:198px;height:456px;background:var(--navy)}
.cover-bar{left:407px;top:0;width:168px;height:28px;background:linear-gradient(#4d4d4f,#2f3033)}
.cover-card{left:423px;top:28px;width:137px;height:140px;background:#fff;display:flex;flex-direction:column;align-items:center;justify-content:center;gap:6px}
.cover-mark{width:14px;height:14px;background:var(--charcoal)}
.cover-name{font-weight:700;font-size:13px;color:var(--charcoal);text-align:center;line-height:1.2}
.tagline{left:423px;top:155px;width:137px;text-align:center;font-style:italic;font-weight:700;font-size:8px;color:var(--charcoal);background:#fff;padding:2px 0 4px}
.phone-box{left:423px;top:408px;width:137px;height:26px;background:#fff;color:var(--charcoal);font-weight:700;font-size:13px;display:flex;align-items:center;justify-content:center;letter-spacing:.5px}
.web-band{left:392px;top:436px;width:198px;height:20px;background:var(--charcoal);color:#fff;font-weight:700;font-size:9px;display:flex;align-items:center;justify-content:center}
/* inside */
.commit-band{left:200px;top:168px;width:390px;height:60px;background:var(--navy);color:#fff;font-size:8.2px;text-align:center;line-height:1.4;display:flex;align-items:center;justify-content:center;letter-spacing:.2px}
.tag-small{position:absolute;background:var(--navy);color:#fff;font-size:6px;padding:2px 5px;letter-spacing:.4px}
</style>
</head>
<body>

<section class="sheet sheet--outside" aria-label="Tri-fold outside">
  <div class="abs panel-quality-top"></div>
  <svg class="abs" style="left:0;top:60px" width="120" height="100" viewBox="0 0 120 100" aria-hidden="true"><polygon points="0,0 120,100 0,100" fill="#fff"/></svg>
  <p class="abs intro"><span class="lead">With more than 20 years combined<br>experience in construction,</span><br><strong class="caps">T&amp;R maintains the absolute<br>highest levels of quality,<br>material, workmanship,<br>and service<br>in each and<br>every project<br>we build.</strong></p>
  <div class="label" style="left:15px;top:108px;width:102px;height:22px">HIGHEST QUALITY</div>
  <div class="photo" role="img" aria-label="Photo of a finished kitchen with dark cabinets and a wooden island bar" style="left:15px;top:160px;width:180px;height:138px;background:linear-gradient(135deg,#1f2a3a,#5a3a28 60%,#8a5a3a)"></div>
  <p class="body-text" style="left:15px;top:310px">A reputation is only as great as the last<br>referral and we understand that the<br>future of our business relies upon<br>satisfied customers. <strong class="caps">We take the time<br>to fully understand our customer’s<br>expectations.</strong> Customer service is more<br>than just<br>a trendy<br>marketing<br>theme, it is<br>the underlying philosophy in everything<br>we do and our home buyers reap the<br>benefits of this philosophy.</p>
  <div class="label" style="left:67px;top:378px;width:116px;height:30px;font-size:8px">100% SATISFACTION<br>GUARANTEED</div>

  <div class="abs panel-detail"></div>
  <div class="photo" role="img" aria-label="Photo of a kitchen with cherry wood cabinets and granite island" style="left:195px;top:218px;width:197px;height:150px;background:linear-gradient(135deg,#3a2418,#7a4a2c 50%,#a57454)"></div>
  <div class="abs values-box"></div>
  <div class="abs owners-card"></div>
  <div class="photo" role="img" aria-label="Small portrait of the two company owners" style="left:293px;top:22px;width:80px;height:56px;background:linear-gradient(#b9b4ae,#3a3a3c)"></div>
  <p class="abs owners-caption">Dan Ortiz &amp; Sam Keller</p>
  <p class="abs values">Throughout our<br>experience we<br>have <strong class="caps">developed lasting<br>values of honesty,<br>real quality, attention<br>to fine detail, efficiency,<br>timeliness, and most of<br>all how to meet a<br>customers expectation<br>by asking the right<br>questions.</strong> With these<br>principles, character and<br>dedication we are able to do<br>things right the first time.</p>
  <div class="label" style="left:285px;top:234px;width:70px;height:18px;font-size:7.5px">FINE DETAIL</div>
  <div class="abs fold-brand">
    <svg width="12" height="12" viewBox="0 0 12 12" aria-hidden="true"><rect width="12" height="12" fill="#fff"/></svg>
    <p class="brand-name">T&amp;R Custom Homes<br>and Remodeling</p>
    <p class="address">1180 Mill Creek Road Suite 4 - Aurora, IL 60500, USA<br>555-014-2290 | www.trhomesbuildco.example</p>
  </div>

  <div class="abs panel-cover"></div>
  <div class="abs cover-bar"></div>
  <div class="abs cover-card">
    <span class="cover-mark" aria-hidden="true"></span>
    <p class="cover-name">T&amp;R Custom Homes<br>and Remodeling</p>
  </div>
  <p class="abs tagline">“Where every detail matters”</p>
  <div class="photo" role="img" aria-label="Photo of an arched front entry with stone columns and double wooden doors" style="left:392px;top:172px;width:183px;height:238px;background:linear-gradient(#8a8f95,#d8d4cc 40%,#5a2a1e 75%,#b8b2a8)"></div>
  <div class="abs phone-box">555-014-2290</div>
  <div class="abs web-band">www.trhomesbuildco.example</div>
</section>

<section class="sheet sheet--inside" aria-label="Tri-fold inside">
  <div class="photo" role="img" aria-label="Photo of a large brick custom home with a green front lawn" style="left:0;top:0;width:395px;height:242px;background:linear-gradient(var(--sky) 0%,#c9d9e6 22%,#b8a690 38%,#8d7d6c 62%,#6f9a44 72%,var(--grass) 100%)"></div>
  <div class="photo" role="img" aria-label="Before photo of a dated front entry door" style="left:395px;top:42px;width:165px;height:125px;background:linear-gradient(90deg,#8a5a3c,#c9c3b6 40%,#8a5a3c)"></div>
  <span class="tag-small" style="left:400px;top:65px">BEFORE</span>
  <div class="abs commit-band caps">T&amp;R is committed to building quality homes<br>with meticulous craftsmanship, custom designs,<br>and thoughtful touches that add<br>to the homeowners’ quality of life.</div>
  <div class="photo" role="img" aria-label="After photo of a renovated stone front porch with a new entry door" style="left:395px;top:232px;width:165px;height:193px;background:linear-gradient(#7c6a5a,#bdb3a6 40%,#9c9488 80%,#c4beb4)"></div>
  <span class="tag-small" style="left:522px;top:281px">AFTER</span>
  <div class="photo" role="img" aria-label="Photo of a wrought iron chandelier hanging in a tall foyer" style="left:103px;top:194px;width:144px;height:109px;background:linear-gradient(135deg,#e8ddcb,#c9b79b)"></div>
  <div class="label" style="left:13px;top:257px;width:110px;height:34px;font-size:8px">HIGHEST LEVEL<br>OF CRAFTSMANSHIP</div>
  <div class="photo" role="img" aria-label="Photo of a bathroom vanity with dark cabinets and granite top" style="left:13px;top:309px;width:158px;height:128px;background:linear-gradient(135deg,#2b1e18,#6b4a34 55%,#c9b89a)"></div>
  <p class="body-text" style="left:248px;top:262px;width:135px;text-align:right">Over the years, we have developed<br>close working relationships with<br>some of the best local craftsmen,<br>vendors, and suppliers located<br>in the western suburbs<br>of Chicago.</p>
  <p class="body-text" style="left:212px;top:344px">These trade partners know<br><strong class="caps">we expect only the highest level<br>of craftsmanship and they are<br>required to perform at only the<br>highest standards of<br>professionalism, accuracy and<br>timeliness.</strong> We take pride in creating<br>homes that are as beautiful to look at,<br>as they are comfortable to live in.</p>
</section>

</body>
</html>
```